Marrowgate Auctions Business Cards Design Needed

I need a business card design that is modern looking - double sided (maybe just my logo on the back, but open to suggestions) - the overall design is up to you. I want it to be easy to read - not over the top flashy. I already have a company logo which I uploaded so that needs to be used. The colors of my logo are the colors I want on the card... so blue and gray (do need to match the logo colors).

Requirements
Must have
• Would like the card to be sleek, modern and easy to ready

```html
<!DOCTYPE html>
<html lang="en">
<head>
<meta charset="utf-8">
<title>Marrowgate Auctions – Business Cards</title>
<link rel="stylesheet" href="https://fonts.googleapis.com/css2?family=Roboto:wght@400;500;700;900&display=swap">
<style>
  :root {
    --brand-blue: #347bb8;
    --brand-blue-dark: #2a659a;
    --brand-gray: #4d4d4f;
    --card-white: #f7f7f7;
    --backdrop: #e4e4e4;
    --white: #ffffff;
  }
  * { box-sizing: border-box; margin: 0; padding: 0; }
  html, body { width: 1200px; height: 726px; overflow: hidden; }
  body {
    background: var(--backdrop);
    font-family: "Roboto", Arial, sans-serif;
    position: relative;
  }
  .card {
    position: absolute;
    top: 203px;
    width: 560px;
    height: 320px;
    overflow: hidden;
  }
  /* Back side */
  .card-back {
    left: 26px;
    background: var(--brand-blue);
    color: var(--white);
    text-align: center;
  }
  .card-back .brand-mark {
    position: absolute;
    left: 0; right: 0; top: 92px;
    display: flex; align-items: center; justify-content: center; gap: 14px;
  }
  .card-back .brand-square {
    width: 34px; height: 34px; background: var(--white);
  }
  .card-back .brand-name {
    font-weight: 900; font-size: 34px; letter-spacing: 1px; text-transform: uppercase;
  }
  .card-back .brand-rule {
    position: absolute; left: 120px; right: 120px; top: 146px;
    height: 2px; background: var(--white);
  }
  .card-back .tagline {
    position: absolute; left: 0; right: 0; top: 156px;
    font-size: 13px; font-weight: 700; letter-spacing: 1px; text-transform: uppercase;
  }
  .card-back .web-row {
    position: absolute; left: 0; right: 0; top: 232px;
    display: flex; align-items: center; justify-content: center; gap: 18px;
    font-size: 16px; letter-spacing: .5px;
  }
  .card-back .web-row .flank { width: 64px; height: 2px; background: var(--white); }

  /* Front side */
  .card-front {
    left: 614px;
    background: var(--card-white);
  }
  .card-front .contact-band {
    position: absolute; left: 150px; right: 0; top: 92px; height: 130px;
    background: var(--brand-blue);
  }
  .card-front .side-strip {
    position: absolute; left: 30px; top: 150px; width: 26px; height: 140px;
    background: var(--brand-blue);
  }
  .card-front .brand-square {
    position: absolute; left: 56px; top: 92px; width: 130px; height: 130px;
    background: var(--brand-gray);
  }
  .card-front .brand-name {
    position: absolute; right: 34px; top: 30px;
    font-weight: 900; font-size: 34px; letter-spacing: .5px; text-transform: uppercase;
    color: var(--brand-gray);
  }
  .card-front .contact {
    position: absolute; right: 30px; top: 104px;
    text-align: right; color: var(--white);
  }
  .contact .person { font-size: 22px; font-weight: 700; }
  .contact .role { font-size: 12px; margin-bottom: 10px; }
  .contact .line {
    display: flex; justify-content: flex-end; align-items: center; gap: 8px;
    font-size: 13px; line-height: 19px;
  }
  .contact .line svg { width: 12px; height: 12px; fill: none; stroke: var(--white); stroke-width: 1.6; }
  .card-front .tagline {
    position: absolute; right: 30px; top: 256px;
    font-size: 15px; font-weight: 500; letter-spacing: .5px; text-transform: uppercase;
    color: var(--brand-blue);
  }
</style>
</head>
<body>
  <section class="card card-back" aria-label="Card back">
    <div class="brand-mark">
      <span class="brand-square"></span>
      <span class="brand-name">Marrowgate Auctions</span>
    </div>
    <div class="brand-rule"></div>
    <p class="tagline">Improving charity auctions nationwide</p>
    <div class="web-row">
      <span class="flank"></span>
      <span>www.bidrevival.com</span>
      <span class="flank"></span>
    </div>
  </section>

  <section class="card card-front" aria-label="Card front">
    <div class="contact-band"></div>
    <div class="side-strip"></div>
    <div class="brand-square"></div>
    <h1 class="brand-name">Marrowgate Auctions</h1>
    <div class="contact">
      <p class="person">Owen Harlow</p>
      <p class="role">Owner/President - Auctioneer</p>
      <p class="line">555-014-2280
        <svg viewBox="0 0 12 12" aria-hidden="true"><path d="M2 1.5h2.5l1 2.5-1.5 1a6 6 0 0 0 3 3l1-1.5 2.5 1v2.5a1 1 0 0 1-1 1A9.5 9.5 0 0 1 1 2.5a1 1 0 0 1 1-1z"/></svg>
      </p>
      <p class="line">info@marrowgatebids.com
        <svg viewBox="0 0 12 12" aria-hidden="true"><rect x="1" y="2.5" width="10" height="7"/><path d="M1 2.5l5 4 5-4"/></svg>
      </p>
      <p class="line">www.bidrevival.com
        <svg viewBox="0 0 12 12" aria-hidden="true"><circle cx="6" cy="6" r="5"/><ellipse cx="6" cy="6" rx="2.2" ry="5"/><path d="M1 6h10"/></svg>
      </p>
    </div>
    <p class="tagline">Improving charity auctions nationwide</p>
  </section>
</body>
</html>
```